Stationery Design Project - Tax Professionals/Chartered Accountants

The name of our firm is “Penwick Group” and our slogan is “Bright Pathways”. You can also use the name "The Penwick Group" if it works better.

We are looking for a full stationery design: Letterhead, Business Card and With Compliments slip

We are looking for a bold, modern and clean/simple design that makes us stand out. We stand out as professionals in the industry and would like the stationery that our clients see to convey this image as well.

There is no colour preference.

We have used a "Lion" as our logo/symbol and that has received positive feedback from our clients; if you think the lion works then please incorporate the "lion".

If you think another symbol works then please submit this we are very open to ideas and would like to see designs that don't incorporate a lion as well.

We would like a corporate feel to this.

You could also incorporate the LG logo http://www.ledgerguildexample.com.au/Members/Marketing-your-practice/Logos but this is not a must.

WHO WE ARE:-
We are a Chartered Accounting firm who specialise in the delivery of taxation and strategic insolvency services. We also provide financial reporting services that help clients negotiate and compromise their debt or expenses such as rent with their landlords.

We work with Law Firms, other Accountants to deliver the best service for our clients.

Our clients come from varied backgrounds and are largely successful and established businesses and high net worth individuals looks for effective tax planning.

We are not the usual accounting firm and do not provide traditional tax return based services.
Updates

Reason: There are still designers who have signed on but not yet submitted designs and also adjustments to existing designs submitted. Extra time so designers are not rushed.

Target Market(s)

Corporate/ Independent successful businesses and individuals

Industry/Entity Type

Business

Requirements
Must have
• The letter must have the following phrase
“Liability limited by a scheme approved under Professional Standards Legislation”

The letter must also have the following business information:-
“The Penwick Group Pty Ltd atf
Principal - Colin T. Penwick
ABN: 47 215 708 362”

Plus Usual Address & Contact Details

We would also a logo or symbol that is representative of us. We like the idea of a lion but this is not set in stone and are very open to ideas.

```html
<!DOCTYPE html>
<html lang="en">
<head>
<meta charset="utf-8">
<title>Penwick Group – Business Card</title>
<link rel="stylesheet" href="https://fonts.googleapis.com/css2?family=Questrial&display=swap">
<style>
  :root {
    --backdrop: #e9e6e2;
    --card-white: #ffffff;
    --card-dark: #2b2b2b;
    --brand-red: #e31e24;
    --ink: #3a3a3a;
    --ink-soft: #555555;
    --paper-text: #ffffff;
  }
  * { box-sizing: border-box; margin: 0; padding: 0; }
  html, body {
    width: 1200px; height: 900px; overflow: hidden;
    background: var(--backdrop);
    font-family: "Questrial", "Century Gothic", sans-serif;
  }
  .canvas {
    position: relative; width: 1200px; height: 900px;
  }
  .card {
    position: absolute; left: 290px; width: 620px; height: 355px;
    box-shadow: 0 6px 18px rgba(0,0,0,0.18);
  }
  /* ---------- back of card ---------- */
  .card--details { top: 70px; background: var(--card-white); color: var(--ink); }
  .brand-mark {
    position: absolute; left: 40px; top: 32px;
    display: flex; align-items: center; gap: 10px;
  }
  .brand-mark__square { width: 18px; height: 18px; background: var(--brand-red); }
  .brand-mark__name { font-size: 20px; color: var(--ink); }
  .holder {
    position: absolute; left: 40px; top: 100px;
  }
  .holder__name { font-size: 22px; letter-spacing: 1px; text-transform: uppercase; }
  .holder__role { font-size: 14px; letter-spacing: 0.5px; text-transform: uppercase; margin-top: 4px; }
  .details-rule {
    position: absolute; left: 0; right: 0; top: 170px; height: 9px;
    background: var(--brand-red);
  }
  .contact-list {
    position: absolute; left: 40px; top: 215px; list-style: none;
    font-size: 14px; line-height: 26px; color: var(--ink-soft);
  }
  .contact-list li { display: flex; align-items: center; gap: 9px; }
  .contact-list svg { width: 12px; height: 12px; fill: var(--ink-soft); }
  .address {
    position: absolute; right: 40px; top: 215px; text-align: right;
    font-size: 14px; line-height: 26px; color: var(--ink-soft); font-style: normal;
  }
  /* ---------- front of card ---------- */
  .card--front { top: 475px; background: var(--card-dark); }
  .front-rule {
    position: absolute; left: 0; top: 148px; width: 340px; height: 11px;
    background: var(--brand-red);
  }
  .front-brand {
    position: absolute; right: 40px; top: 126px;
    display: flex; align-items: center; gap: 14px;
  }
  .front-brand__square { width: 54px; height: 54px; background: var(--brand-red); }
  .front-brand__name { font-size: 38px; color: var(--paper-text); }
  .front-tagline {
    position: absolute; right: 40px; top: 210px;
    font-size: 15px; color: var(--paper-text); letter-spacing: 0.5px;
  }
</style>
</head>
<body>
<main class="canvas">
  <section class="card card--details" aria-label="Business card, contact side">
    <div class="brand-mark">
      <span class="brand-mark__square"></span>
      <span class="brand-mark__name">Penwick Group</span>
    </div>
    <div class="holder">
      <p class="holder__name">Daniel Whitcombe</p>
      <p class="holder__role">IT Consultant</p>
    </div>
    <div class="details-rule"></div>
    <ul class="contact-list">
      <li>
        <svg viewBox="0 0 12 12" aria-hidden="true"><path d="M2.5 0.8 4.3 3 3.4 4.3c.7 1.6 2.1 3 3.7 3.7L8.4 7l2.2 1.8-.9 2.1C5.3 11 .9 6.6 1 2z"/></svg>
        +441132049617
      </li>
      <li>
        <svg viewBox="0 0 12 12" aria-hidden="true"><path d="M0 2.5h12v7H0zM1 3.3v.3l5 3 5-3v-.3z"/></svg>
        daniel.whitcombe@penwickmail.com
      </li>
      <li>
        <svg viewBox="0 0 12 12" aria-hidden="true"><path d="M6 0a6 6 0 1 0 0 12A6 6 0 0 0 6 0zm0 1.2c.8 0 1.5 1.9 1.6 4.2H4.4C4.5 3.1 5.2 1.2 6 1.2zM4.4 6.6h3.2c-.1 2.3-.8 4.2-1.6 4.2s-1.5-1.9-1.6-4.2z"/></svg>
        www.penwickgroup.com
      </li>
    </ul>
    <address class="address">
      Kiln House, Weaver Road,<br>
      Leeds, LS10 3TR
    </address>
  </section>

  <section class="card card--front" aria-label="Business card, brand side">
    <div class="front-rule"></div>
    <div class="front-brand">
      <span class="front-brand__square"></span>
      <span class="front-brand__name">Penwick Group</span>
    </div>
    <p class="front-tagline">bright pathways</p>
  </section>
</main>
</body>
</html>
```